Business Card Design for Small Electrical Contractor

I need to update my business card into something a little more modern. We are a small electrical contracting company. We service domestic and commercial places around Sydney. We have 2 logo designs at the moment. I have uploaded both and 2 different sizes to work with.

Industry/Entity Type

Business

Contact Information for Business Card

Leo Hartigan
8/21-23 Birch Rd, Kelsworth 2087
t - (02) 9381 4720
m - 0427 815 903
E - info@hartiganelx.com.au
W - hartiganelx.com.au
ABN: 42 907 551 316

Font styles to use
Sans Serif

Requirements
Must have
• I would also like to see the below fit on somewhere aswell
• - Licensed Electrician
• - Level 2 (Cat 1 & 4)
• - Domestic
• - Commercial
• - Repairs and Installations
• - Data
Nice to have
• Try and keep similar colours as logo
Should not have
• No lightning bolts or light globes. Smart and professional please.

```html
<!DOCTYPE html>
<html lang="en">
<head>
<meta charset="utf-8">
<title>Hartigan Electrical – Business Card</title>
<link rel="stylesheet" href="https://fonts.googleapis.com/css2?family=Montserrat:wght@400;500;600;700&display=swap">
<style>
  :root {
    --backdrop: #8c8c8c;
    --card-white: #ffffff;
    --card-black: #070707;
    --ink: #1c3530;
    --accent: #f39a24;
    --text-light: #ffffff;
  }
  * { margin: 0; padding: 0; box-sizing: border-box; }
  html, body { width: 1200px; height: 852px; overflow: hidden; }
  body {
    background: var(--backdrop);
    font-family: "Montserrat", Arial, sans-serif;
    position: relative;
  }
  .card {
    position: absolute;
    border-radius: 14px;
    overflow: hidden;
  }
  .card--front {
    left: 320px; top: 48px; width: 546px; height: 335px;
    background: var(--card-white);
    color: var(--ink);
  }
  .card--back {
    left: 318px; top: 446px; width: 552px; height: 338px;
    background: var(--card-black);
    color: var(--text-light);
  }
  .brand-name {
    font-weight: 600;
    font-size: 30px;
    letter-spacing: 0.5px;
    white-space: nowrap;
    line-height: 1;
  }
  .card--front .brand-name { position: absolute; left: 38px; top: 40px; color: var(--ink); }
  .card--front .brand-rule {
    position: absolute; left: 38px; top: 84px; width: 248px; height: 1.5px;
    background: var(--accent);
  }
  .abn {
    position: absolute; left: 38px; top: 111px;
    font-size: 12px; font-weight: 500; letter-spacing: 0.3px;
  }
  .person-name {
    position: absolute; right: 34px; top: 122px;
    font-size: 20px; font-weight: 700;
  }
  .contact-list {
    position: absolute; right: 26px; top: 173px;
    list-style: none;
  }
  .contact-list li, .address {
    display: flex; align-items: center; justify-content: flex-end;
    font-size: 17px; font-weight: 500; letter-spacing: 0.3px;
    height: 24px;
  }
  .address {
    position: absolute; right: 26px; top: 287px;
    font-size: 15.5px;
  }
  .icon {
    width: 17px; height: 17px; margin-left: 9px;
    fill: none; stroke: var(--accent); stroke-width: 2;
    flex-shrink: 0;
  }
  .icon--solid { fill: var(--accent); stroke: none; }

  .card--back .brand-name {
    position: absolute; left: 0; right: 0; top: 56px;
    text-align: center; color: var(--text-light);
  }
  .card--back .brand-rule {
    position: absolute; left: 146px; top: 121px; width: 260px; height: 1.5px;
    background: var(--accent);
  }
  .licence-band {
    position: absolute; left: 0; top: 160px; width: 100%; height: 25px;
    background: var(--accent);
    text-align: center;
    font-size: 18.5px; font-weight: 600; line-height: 27px;
  }
  .services {
    position: absolute; left: 0; right: 0; top: 201px;
    list-style: none; text-align: center;
  }
  .services li {
    font-size: 15.5px; font-weight: 600; letter-spacing: 0.2px;
    height: 38px; word-spacing: 1px;
  }
  .services span + span { margin-left: 10px; }
</style>
</head>
<body>

<section class="card card--front" aria-label="Business card front">
  <div class="brand-name">Hartigan Electrical</div>
  <div class="brand-rule"></div>
  <p class="abn">ABN: 42 907 551 316</p>

  <h1 class="person-name">Leo Hartigan</h1>

  <ul class="contact-list">
    <li>(02) 9381 4720
      <svg class="icon icon--solid" viewBox="0 0 24 24"><path d="M6.6 10.8a15 15 0 0 0 6.6 6.6l2.2-2.2a1 1 0 0 1 1-.25 11.4 11.4 0 0 0 3.6.57 1 1 0 0 1 1 1V20a1 1 0 0 1-1 1A17 17 0 0 1 3 4a1 1 0 0 1 1-1h3.5a1 1 0 0 1 1 1c0 1.25.2 2.45.57 3.57a1 1 0 0 1-.25 1z"/></svg>
    </li>
    <li>0427 815 903
      <svg class="icon" viewBox="0 0 24 24"><rect x="6" y="2" width="12" height="20" rx="2"/><line x1="11" y1="18.5" x2="13" y2="18.5"/></svg>
    </li>
    <li>info@hartiganelx.com.au
      <svg class="icon icon--solid" viewBox="0 0 24 24"><path d="M2 5h20v14H2z" fill="var(--accent)"/><path d="M2 5l10 8 10-8" fill="none" stroke="#fff" stroke-width="1.6"/></svg>
    </li>
    <li>hartiganelx.com.au
      <svg class="icon" viewBox="0 0 24 24" stroke-width="1.6"><circle cx="12" cy="12" r="9"/><ellipse cx="12" cy="12" rx="4" ry="9"/><line x1="3" y1="12" x2="21" y2="12"/><path d="M5 7h14M5 17h14"/></svg>
    </li>
  </ul>

  <p class="address">8/21-23 Birch Rd, Kelsworth 2087
    <svg class="icon icon--solid" viewBox="0 0 24 24" style="height:20px"><path d="M12 2a7 7 0 0 0-7 7c0 5 7 13 7 13s7-8 7-13a7 7 0 0 0-7-7zm0 9.5A2.5 2.5 0 1 1 12 6.5a2.5 2.5 0 0 1 0 5z"/></svg>
  </p>
</section>

<section class="card card--back" aria-label="Business card back">
  <div class="brand-name">Hartigan Electrical</div>
  <div class="brand-rule"></div>
  <div class="licence-band">Licensed Electrician</div>
  <ul class="services">
    <li>• Level 2 (Cat 1 &amp; 4)</li>
    <li><span>• Domestic</span><span>• Commercial</span></li>
    <li><span>• Repairs and Installations</span><span>• Data</span></li>
  </ul>
</section>

</body>
</html>
```